Road Construction Company needs business cards

We would like a new business card designed for our business.

We're a road construction company based in Qld, Australia.

Can the business card please have the following information on it.

Name: Brent Malvoy
Position: General Manager
Phone: 0471 592 304
Email: Brent.malvoy@quendix.com.au
Address: 87 Harrowgate Ave, Pindarra, QLD, 4000
Website: www.quendix.com.au

Visually we'd like the card to be professional and simple.

Attached is our logo.

Our website is www.quendix.com.au

Target Market(s)

Men aged 25-60

Contact Information for Business Card

As listed in project description

Font styles to use
Serif

Requirements
Must have
• Large logo on back of card

```html
<!DOCTYPE html>
<html lang="en">
<head>
<meta charset="utf-8">
<title>Quendix Business Card</title>
<link rel="stylesheet" href="https://fonts.googleapis.com/css2?family=Fira+Sans:wght@400;600;800&display=swap">
<style>
  :root {
    --navy: #0b4f9c;
    --sky: #3a9bd5;
    --paper: #ffffff;
    --backdrop: #8e9195;
  }
  * { margin: 0; padding: 0; box-sizing: border-box; }
  html, body { width: 1200px; height: 1200px; overflow: hidden; }
  body {
    background: var(--backdrop);
    position: relative;
    font-family: "Fira Sans", sans-serif;
  }
  .card {
    position: absolute;
    width: 636px;
    height: 403px;
    background: var(--paper);
    overflow: hidden;
  }
  .card--front { left: 156px; top: 151px; }
  .card--back  { left: 373px; top: 672px; }

  .brand-name {
    position: absolute;
    left: 0; right: 0;
    top: 160px;
    text-align: center;
    font-size: 62px;
    font-weight: 800;
    letter-spacing: 2px;
    color: var(--navy);
    line-height: 1;
  }

  .person-name {
    position: absolute;
    left: 0; right: 0; top: 92px;
    text-align: center;
    font-size: 24px;
    font-weight: 600;
    color: var(--navy);
    line-height: 1;
  }
  .person-role {
    position: absolute;
    left: 0; right: 0; top: 120px;
    text-align: center;
    font-size: 19px;
    font-weight: 400;
    color: var(--sky);
    line-height: 1;
  }
  .icon-rail {
    position: absolute;
    left: 154px; top: 162px;
    width: 327px; height: 30px;
  }
  .contact-list {
    position: absolute;
    left: 0; right: 0; top: 206px;
    list-style: none;
    text-align: center;
    color: var(--navy);
    font-size: 15px;
    font-weight: 400;
  }
  .contact-list li { height: 28px; line-height: 20px; }
  .accent-band {
    position: absolute;
    left: 0; bottom: 0;
    width: 100%; height: 7px;
    display: flex;
  }
  .accent-band span { flex: 1; }
  .accent-band .accent-dark { background: var(--navy); }
  .accent-band .accent-light { background: var(--sky); }
</style>
</head>
<body>
  <section class="card card--front">
    <div class="brand-name">QUENDIX</div>
  </section>

  <section class="card card--back">
    <h1 class="person-name">BRENT MALVOY</h1>
    <p class="person-role">General Manager</p>

    <svg class="icon-rail" viewBox="0 0 327 30" aria-hidden="true">
      <g stroke="var(--navy)" stroke-width="2">
        <line x1="0" y1="15" x2="79" y2="15"/>
        <line x1="107" y1="15" x2="126" y2="15"/>
        <line x1="154" y1="15" x2="173" y2="15"/>
        <line x1="201" y1="15" x2="219" y2="15"/>
        <line x1="247" y1="15" x2="327" y2="15"/>
      </g>
      <g fill="var(--navy)">
        <circle cx="93" cy="15" r="14"/>
        <circle cx="140" cy="15" r="14"/>
        <circle cx="187" cy="15" r="14"/>
        <circle cx="233" cy="15" r="14"/>
      </g>
      <!-- phone -->
      <path d="M85 14 q8 -7 16 0 l-2 2 -3 -1 0 -2 q-3 -1 -6 0 l0 2 -3 1 z M88 16 h10 v4 h-10 z" fill="#fff"/>
      <!-- mail -->
      <rect x="133" y="10" width="14" height="10" fill="#fff"/>
      <polyline points="133,10 140,16 147,10" fill="none" stroke="var(--navy)" stroke-width="1.2"/>
      <!-- globe -->
      <g fill="none" stroke="#fff" stroke-width="1.3">
        <circle cx="187" cy="15" r="7"/>
        <ellipse cx="187" cy="15" rx="3" ry="7"/>
        <line x1="180" y1="15" x2="194" y2="15"/>
      </g>
      <!-- pin -->
      <path d="M233 24 l-5 -7 a6 6 0 1 1 10 0 z" fill="#fff"/>
      <circle cx="233" cy="13" r="2.2" fill="var(--navy)"/>
    </svg>

    <ul class="contact-list">
      <li>0471 592 304</li>
      <li>Brent.malvoy@quendix.com.au</li>
      <li>www.quendix.com.au</li>
      <li>87 Harrowgate Ave, Pindarra, QLD, 4000</li>
    </ul>

    <div class="accent-band">
      <span class="accent-dark"></span>
      <span class="accent-light"></span>
    </div>
  </section>
</body>
</html>
```